Power Point Template for Unique Indoor Advertising Company.

We need PowerPoint slide templates for our Sales Media Kit at our re-branded company based in Canada called "Bellwether Ad Collective".

Looking for a look that clearly and powerfully portrays our unique and effective indoor advertising billboards in our network.

Our Prime Billboards are strategically placed in high traffic areas of restaurants, pubs, nightclubs, fitness clubs, colleges and universities, and sports arenas.

Key features of our media is a captive audience and 100% gender specific.

You can visit our current website for info on our media (foxglovepromotions.ca)

Our Media Kits go out to small, medium business owners and advertising agenices and need to be eye-catching, trendy and slick.

Our logos are attached.

Deliverables are:

1) Presentation cover slide with rich graphic content and space for content.
2) Presentation body slide with room for content, 3-4 photos. This slide should have the following:
a) No graphic in the text area
b) Space for page number at the bottom.
3) Photoshop (PSD) files for all graphic elements.
4) Font files for all fonts used.

Target Market(s)

Advertising Agencies and Media Buyers

Industry/Entity Type

It Company

Font styles to use
Serif

Requirements
Must have
• Captivating and sleek look that is eye-catching and targeted.

```html
<!DOCTYPE html>
<html lang="en">
<head>
<meta charset="utf-8">
<title>Bellwether Ad Collective – Media Kit Slides</title>
<link href="https://fonts.googleapis.com/css2?family=Roboto+Slab:wght@400;600;700&family=Noto+Serif:wght@400;700&display=swap" rel="stylesheet">
<style>
:root{
  --red:#c8161d;
  --red-dark:#7e0c11;
  --ink:#2e2e2e;
  --grey-mid:#8c8c8c;
  --grey-light:#d9d9d9;
  --paper:#ffffff;
  --panel:#585858;
  --footer:#7a7a7a;
  --head:"Roboto Slab",Georgia,serif;
  --body:"Noto Serif",Georgia,serif;
  --ph-warm:linear-gradient(155deg,#f0d3a8 0%,#b7794a 45%,#4a2b1c 100%);
  --ph-amber:linear-gradient(200deg,#ffcf8a 0%,#a85f2a 50%,#2f1a12 100%);
  --ph-cool:linear-gradient(160deg,#f4f4f2 0%,#bfc3c6 45%,#5e6569 100%);
  --ph-dark:linear-gradient(150deg,#6a5a52 0%,#2c2220 55%,#0e0b0b 100%);
  --ph-red:linear-gradient(150deg,#e9787b 0%,#a3161c 50%,#3a0508 100%);
  --ph-crowd:linear-gradient(170deg,#c9b59c 0%,#6e5646 50%,#231915 100%);
}
*{box-sizing:border-box;margin:0;padding:0}
html,body{width:1200px;height:3916px;overflow:hidden;background:#fff}
body{font-family:var(--body);color:var(--ink)}
.deck{display:grid;grid-template-columns:repeat(3,392px);grid-auto-rows:222px;gap:8px;padding:4px}
.slide{position:relative;overflow:hidden;background:var(--paper);box-shadow:0 0 0 1px #e2e2e2}
.slide.dark{background:var(--panel);color:#fff}
.a{position:absolute}
.s-title{position:absolute;left:14px;top:12px;font-family:var(--head);font-size:13px;font-weight:600;color:var(--ink);white-space:nowrap}
.s-title .u{border-bottom:2px solid var(--red);padding-bottom:1px}
.big-t{font-family:var(--head);font-weight:600;line-height:1.15}
.brand{position:absolute;top:10px;right:12px;display:flex;align-items:center;gap:4px;font-family:var(--head);font-size:7.5px;font-weight:700;color:var(--red);white-space:nowrap}
.brand::before{content:"";width:7px;height:7px;border-radius:50%;background:var(--red)}
.brand.w{color:#fff}.brand.w::before{background:#fff}
.brand.st{position:static}
.foot{position:absolute;left:0;right:0;bottom:0;height:9px;background:var(--footer);font-size:4.5px;color:#eee;padding-left:8px;line-height:9px}
.foot::after{content:"";position:absolute;right:0;top:0;width:14px;height:9px;background:var(--red)}
.ph{position:absolute;background:var(--ph-crowd);box-shadow:inset 0 0 24px rgba(0,0,0,.25)}
.ph.warm{background:var(--ph-warm)}
.ph.amber{background:var(--ph-amber)}
.ph.cool{background:var(--ph-cool)}
.ph.dk{background:var(--ph-dark)}
.ph.rd{background:var(--ph-red)}
.p{font-size:5.2px;line-height:1.55;color:#777}
.dark .p{color:#ddd}
.h{font-family:var(--head);font-size:6.8px;font-weight:700;color:var(--ink)}
.dark .h{color:#fff}
.lead{font-size:7px;color:var(--ink)}
.lead b{color:var(--red)}
.ic{display:inline-block;flex:none;width:13px;height:13px;border-radius:50%;background:var(--red);position:relative}
.ic::after{content:"";position:absolute;left:4.5px;top:2.5px;width:3px;height:6px;border:solid #fff;border-width:0 1.5px 1.5px 0;transform:rotate(45deg)}
.ic.g{background:var(--grey-mid)}
.it{display:flex;gap:6px;align-items:flex-start;margin-bottom:8px}
.it b{display:block;font-family:var(--head);font-size:6.2px;color:var(--ink)}
.dark .it b{color:#fff}
.it p{font-size:4.8px;color:#888;line-height:1.5}
.dark .it p{color:#ddd}
.sq{display:inline-block;flex:none;width:5px;height:5px;background:var(--red);margin:2px 4px 0 0}
.band-red{position:absolute;background:var(--red);color:#fff}
.num{display:inline-flex;align-items:center;justify-content:center;width:16px;height:16px;background:var(--red);color:#fff;font-family:var(--head);font-size:8px;font-weight:700;flex:none}
.cols{position:absolute;display:grid;gap:12px}
table{border-collapse:collapse;width:100%}
</style>
</head>
<body>
<main class="deck">

<section class="slide">
  <div class="ph rd" style="inset:0" role="img" aria-label="Red-toned photo of a busy venue interior"></div>
  <div class="a" style="left:0;right:0;top:62px;text-align:center">
    <div class="brand w st" style="justify-content:center;font-size:20px;gap:8px">Bellwether Ad Collective</div>
    <div style="margin-top:6px;font-size:6.5px;color:#fff">Over 1,000 Billboards | 3 Targeted Networks | Regional Coverage</div>
  </div>
</section>

<section class="slide">
  <div class="ph crowd" style="left:0;top:0;right:0;height:120px" role="img" aria-label="Photo of a convention hall crowd"></div>
  <div class="a" style="left:136px;top:6px;width:120px;height:20px;background:#fff;display:flex;align-items:center;justify-content:center"><span class="brand st">Bellwether Ad Collective</span></div>
  <div class="band-red big-t" style="left:0;right:0;top:120px;height:34px;font-size:13px;text-align:center;line-height:34px">Your Title Goes Here</div>
  <div class="a" style="left:30px;top:166px;right:30px;display:flex;justify-content:space-between;font-size:5.5px;line-height:1.5">
    <div><b>Avery Lin</b><br>Presenter</div><div><b>Morgan Hale</b><br>Presenter</div><div><b>Riley Park</b><br>Presenter</div>
  </div>
  <div class="foot"></div>
</section>

<section class="slide">
  <div class="ph cool" style="inset:0" role="img" aria-label="Photo of a bright gallery interior"></div>
  <div class="a" style="left:106px;top:36px;width:180px;height:34px;background:#fff;display:flex;align-items:center;justify-content:center"><span class="brand st" style="font-size:10px">Bellwether Ad Collective</span></div>
  <div class="band-red big-t" style="left:50px;right:50px;top:78px;height:28px;text-align:center;font-size:12px;line-height:28px">Your Title Goes Here</div>
  <div class="a" style="left:0;right:0;top:110px;text-align:center;font-size:5.5px;color:#333">Presented by Avery Lin</div>
</section>

<section class="slide">
  <div class="ph cool" style="inset:0 0 60px 0" role="img" aria-label="Black and white photo of a large hall"></div>
  <div class="brand" style="left:12px;right:auto">Bellwether Ad Collective</div>
  <div class="a big-t" style="left:0;right:0;bottom:20px;height:40px;background:#fff;text-align:center;font-size:13px;line-height:40px">Your Title Goes Here</div>
  <div class="a" style="left:0;right:0;bottom:10px;height:10px;background:var(--red)"></div>
  <div class="foot"></div>
</section>

<section class="slide">
  <div class="ph warm" style="left:0;top:0;width:220px;bottom:0;opacity:.6" role="img" aria-label="Faded photo of a venue interior"></div>
  <div class="brand" style="left:12px;right:auto">Bellwether Ad Collective</div>
  <div class="a big-t" style="left:236px;top:74px;font-size:14px">Your Title<br>Goes Here</div>
  <div class="a" style="left:236px;top:112px;font-size:5.5px;color:var(--red)">Your Subtitle Goes Here</div>
  <div class="a" style="left:280px;top:156px;font-size:5.2px;line-height:1.6"><b>Presented by</b><br>Morgan Hale<br>Account Lead</div>
  <div class="foot"></div>
</section>

<section class="slide">
  <div class="s-title"><span class="u">Our</span> Agenda</div>
  <div class="brand">Bellwether Ad Collective</div>
  <div class="cols" style="left:40px;top:50px;right:30px;grid-template-columns:1fr 1fr;row-gap:14px">
    <div class="it"><span class="num">1</span><div><b>Agenda One</b><p>Short note on this item.</p></div></div>
    <div class="it"><span class="num">4</span><div><b>Agenda Four</b><p>Short note on this item.</p></div></div>
    <div class="it"><span class="num">2</span><div><b>Agenda Two</b><p>Short note on this item.</p></div></div>
    <div class="it"><span class="num">5</span><div><b>Agenda Five</b><p>Short note on this item.</p></div></div>
    <div class="it"><span class="num">3</span><div><b>Agenda Three</b><p>Short note on this item.</p></div></div>
    <div class="it"><span class="num">6</span><div><b>Agenda Six</b><p>Short note on this item.</p></div></div>
  </div>
  <div class="foot"></div>
</section>

<section class="slide">
  <div class="ph cool" style="left:0;top:0;width:230px;bottom:0" role="img" aria-label="Photo of an indoor billboard in a bright mall"></div>
  <div class="a" style="left:30px;top:62px;width:170px;height:30px;background:#fff;display:flex;align-items:center;justify-content:center"><span class="brand st" style="font-size:10px">Bellwether Ad Collective</span></div>
  <div class="a" style="left:230px;top:0;right:0;bottom:0;background:var(--panel)"></div>
  <div class="a" style="left:242px;top:30px;right:12px;color:#fff">
    <div class="big-t" style="font-size:12px;margin-bottom:8px">About Us</div>
    <p class="p" style="color:#e5e5e5">Indoor billboards placed where people stay. Our frames reach a captive crowd in pubs, gyms and arenas across Canada.</p>
    <p class="p" style="color:#e5e5e5;margin-top:6px">Every network is gender specific, so each message meets the right audience.</p>
  </div>
  <div class="foot"></div>
</section>

<section class="slide dark">
  <div class="a" style="left:0;top:0;right:0;height:34px;background:#fff"></div>
  <div class="s-title"><span class="u">Our</span> Vision &amp; Mission</div>
  <div class="brand">Bellwether Ad Collective</div>
  <div class="cols" style="left:20px;top:44px;right:20px;grid-template-columns:1fr 1fr;gap:20px">
    <div><div class="h">• Our Vision:</div><p class="p">Go to the next level without losing heart in the work.</p>
      <div class="it" style="margin-top:10px"><span class="ic"></span><div><b>Your Text Here</b><p>Short line of sample text.</p></div></div>
      <div class="it"><span class="ic g"></span><div><b>Your Text Here</b><p>Short line of sample text.</p></div></div></div>
    <div><div class="h">• Our Missions</div>
      <div class="it" style="margin-top:6px"><span class="ic"></span><div><b>Your Text Here</b><p>Short line of sample text.</p></div></div>
      <div class="it"><span class="ic g"></span><div><b>Your Text Here</b><p>Short line of sample text.</p></div></div>
      <div class="it"><span class="ic"></span><div><b>Your Text Here</b><p>Short line of sample text.</p></div></div></div>
  </div>
  <div class="foot"></div>
</section>

<section class="slide">
  <div class="s-title"><span class="u">Quote</span> Area</div>
  <div class="brand">Bellwether Ad Collective</div>
  <div class="a" style="left:0;top:40px;width:200px;height:120px;background:var(--panel);color:#fff;padding:26px 18px;font-size:7px;line-height:1.6;border-left:4px solid var(--red)">Coming together is a beginning.<br>Keeping together is progress.<br>Working together is success.</div>
  <div class="ph warm" style="left:200px;top:40px;right:0;height:150px" role="img" aria-label="Photo of a row of framed indoor ads"></div>
  <div class="foot"></div>
</section>

<section class="slide">
  <div class="s-title"><span class="u">Text</span> Area</div>
  <div class="brand">Bellwether Ad Collective</div>
  <div class="a" style="left:36px;top:44px;right:28px">
    <div class="lead">We are <b>Bellwether Ad Collective</b></div>
    <div class="lead" style="margin-bottom:9px">Over 1,000 Billboards | 3 Targeted Networks | Regional Coverage</div>
    <p class="p">Our indoor billboards sit in restaurants, pubs, nightclubs, fitness clubs, colleges and sports arenas. Guests stay for a while, so your ad is seen again and again by the same crowd.</p>
    <p class="p" style="margin-top:6px">Each placement is gender specific, giving media buyers a clear and measured audience for every campaign.</p>
    <p class="p" style="margin-top:6px">Ask us for venue lists, rates and sample creative for your next launch.</p>
  </div>
  <div class="foot"></div>
</section>

<section class="slide dark">
  <div class="ph dk" style="inset:0" role="img" aria-label="Dark photo of a crowded room"></div>
  <div class="a" style="left:178px;top:40px;width:36px;height:36px;border-radius:50%;background:var(--red);color:#fff;font-family:var(--head);font-size:22px;text-align:center;line-height:44px;font-weight:700">“</div>
  <div class="a" style="left:0;right:0;top:88px;text-align:center;font-size:9.5px;line-height:1.5;color:#fff">Coming together is a beginning.<br>Keeping together is progress.<br>Working together is success.</div>
  <div class="a" style="left:0;right:0;top:146px;text-align:center;font-size:5.2px;color:#ccc">Henry Ford</div>
  <div class="foot"></div>
</section>

<section class="slide">
  <div class="a" style="right:0;top:0;bottom:0;width:12px;background:var(--red)"></div>
  <div class="a" style="left:0;right:0;top:0;height:6px;background:var(--red)"></div>
  <div class="ph crowd" style="left:170px;top:6px;width:80px;height:30px" role="img" aria-label="Venue photo strip"></div>
  <div class="s-title" style="top:20px"><span class="u">Text</span> Area</div>
  <div class="brand" style="top:20px;right:22px">Bellwether Ad Collective</div>
  <div class="a" style="left:16px;top:54px;right:30px">
    <p class="p">Our indoor billboards sit in busy venues where guests stay for a while, so your ad is seen again and again by the same crowd.</p>
    <p class="p" style="margin-top:6px">Each placement is gender specific, giving buyers a clear and measured audience for every campaign they plan.</p>
    <p class="p" style="margin-top:6px">Ask us for venue lists, rates and sample creative.</p>
  </div>
  <div class="foot"></div>
</section>

<section class="slide">
  <div class="s-title"><span class="u">Our</span> Services</div>
  <div class="brand">Bellwether Ad Collective</div>
  <div class="ph warm" style="left:20px;top:42px;width:160px;height:110px" role="img" aria-label="Photo of a lit billboard on a wall"></div>
  <div class="a h" style="left:30px;top:158px">Your Title Goes Here</div>
  <div class="a" style="left:200px;top:48px;right:14px">
    <div class="it"><span class="ic"></span><div><b>Service Number One</b><p>Short line of sample text here.</p></div></div>
    <div class="it"><span class="ic g"></span><div><b>Service Number Two</b><p>Short line of sample text here.</p></div></div>
    <div class="it"><span class="ic"></span><div><b>Service Number Three</b><p>Short line of sample text here.</p></div></div>
  </div>
  <div class="foot"></div>
</section>

<section class="slide">
  <div class="s-title">Your Title <span class="u">Goes Here</span></div>
  <div class="brand">Bellwether Ad Collective</div>
  <div class="ph amber" style="left:20px;top:38px;width:90px;height:72px" role="img" aria-label="Photo of a building"></div>
  <div class="ph cool" style="left:20px;top:114px;width:90px;height:72px" role="img" aria-label="Photo of a lobby"></div>
  <div class="ph rd" style="left:114px;top:114px;width:90px;height:72px" role="img" aria-label="Photo of a sports arena"></div>
  <div class="band-red" style="left:114px;top:38px;width:90px;height:72px;padding:8px"><b style="font-family:var(--head);font-size:6px">Heading Goes Here</b><p style="font-size:4.8px;margin-top:4px;color:#fbdcdc">Short line of sample text.</p></div>
  <div class="ph crowd" style="left:208px;top:38px;width:166px;height:148px" role="img" aria-label="Photo of a stadium crowd"></div>
  <div class="foot"></div>
</section>

<section class="slide">
  <div class="brand" style="left:12px;right:auto">Bellwether Ad Collective</div>
  <div class="s-title" style="top:28px">Your Title <span class="u">Goes Here</span></div>
  <div class="a" style="left:24px;top:60px;width:170px">
    <div class="it"><span class="ic"></span><div><b>Heading Here</b><p>Short line of sample text here.</p></div></div>
    <div class="it"><span class="ic g"></span><div><b>Heading Here</b><p>Short line of sample text here.</p></div></div>
    <div class="it"><span class="ic"></span><div><b>Heading Here</b><p>Short line of sample text here.</p></div></div>
  </div>
  <div class="ph cool" style="left:220px;top:0;right:0;height:150px" role="img" aria-label="Photo of a billboard in a hallway"></div>
  <div class="foot"></div>
</section>

<section class="slide dark">
  <div class="ph dk" style="inset:0" role="img" aria-label="Dark photo of a nightclub"></div>
  <div class="brand w" style="left:14px;right:auto">Bellwether Ad Collective</div>
  <div class="a" style="left:150px;top:38px;right:20px;font-size:6.8px;line-height:1.6;color:#fff">We are Bellwether Ad Collective<br>• Over 1,000 Billboards<br>• 3 Targeted Networks<br>• Regional Coverage</div>
  <div class="a" style="left:150px;top:104px;right:20px">
    <div class="it"><span class="ic"></span><div><b>Your Text Here</b><p>Short line of sample text.</p></div></div>
    <div class="it"><span class="ic"></span><div><b>Your Text Here</b><p>Short line of sample text.</p></div></div>
  </div>
  <div class="foot"></div>
</section>

<section class="slide">
  <div class="ph dk" style="left:0;top:0;width:150px;bottom:0" role="img" aria-label="Photo of a digital display screen in a venue"></div>
  <div class="brand w" style="left:14px;top:172px;right:auto;font-size:8px">Bellwether Ad Collective</div>
  <div class="brand">Bellwether Ad Collective</div>
  <div class="s-title" style="left:166px;top:34px"><span class="u">Your</span> Title Goes Here</div>
  <div class="a" style="left:166px;top:62px;right:18px">
    <div class="it"><span class="ic"></span><div><b>Your Text Goes Here</b><p>Short line of sample text here.</p></div></div>
    <div class="it"><span class="ic g"></span><div><b>Your Text Goes Here</b><p>Short line of sample text here.</p></div></div>
  </div>
  <div class="foot"></div>
</section>

<section class="slide">
  <div class="ph cool" style="left:0;top:0;width:130px;height:110px" role="img" aria-label="Photo of a mall atrium"></div>
  <div class="ph amber" style="left:132px;top:0;width:150px;height:110px" role="img" aria-label="Photo of a tall building"></div>
  <div class="ph crowd" style="left:0;top:112px;width:282px;bottom:9px" role="img" aria-label="Photo of a dining crowd"></div>
  <div class="brand">Bellwether Ad Collective</div>
  <div class="a big-t" style="left:292px;top:40px;font-size:12px">Your Title<br>Goes Here</div>
  <div class="a" style="left:292px;top:78px;width:88px"><p class="p">Short text to sum up this photo set in a line or two.</p></div>
  <div class="foot"></div>
</section>

<section class="slide">
  <div class="s-title"><span class="u">Your</span> Title Goes Here</div>
  <div class="brand">Bellwether Ad Collective</div>
  <div class="a" style="left:22px;top:42px;width:168px;font-size:6.5px;line-height:1.8">We are <b style="color:var(--red)">Bellwether Ad Collective</b><br><span class="sq"></span>Over 1,000 Billboards<br><span class="sq"></span>3 Targeted Networks<br><span class="sq"></span>Regional Coverage
    <p class="p" style="margin-top:8px">Short text about the network and its reach goes here.</p></div>
  <div class="ph amber" style="left:200px;top:38px;width:84px;height:152px" role="img" aria-label="Photo of a bar interior"></div>
  <div class="ph cool" style="left:288px;top:38px;width:88px;height:152px" role="img" aria-label="Photo of a billboard frame"></div>
  <div class="foot"></div>
</section>

<section class="slide">
  <div class="s-title">Your Title <span class="u">Goes Here</span></div>
  <div class="brand">Bellwether Ad Collective</div>
  <div class="a" style="left:20px;top:46px;width:120px"><div class="h">Heading Goes Here</div><p class="p">Short line of sample text for this part.</p></div>
  <svg class="a" style="left:120px;top:80px" width="100" height="90" viewBox="0 0 100 90"><path d="M96 10 C40 20 40 70 96 80" fill="none" stroke="#bbb" stroke-width="1"/><circle cx="67" cy="22" r="3" fill="#c8161d"/><circle cx="55" cy="45" r="3" fill="#c8161d"/><circle cx="67" cy="68" r="3" fill="#c8161d"/></svg>
  <div class="a" style="left:110px;top:96px;width:66px;text-align:right;font-family:var(--head);font-size:5.5px;font-weight:700;line-height:2.4">Your Text Here<br>Your Text Here<br>Your Text Here</div>
  <div class="ph warm" style="left:216px;top:36px;width:110px;height:154px" role="img" aria-label="Photo of a person holding a sign"></div>
  <div class="foot"></div>
</section>

<section class="slide">
  <div class="s-title"><span class="u">Portfolio</span> Area</div>
  <div class="brand">Bellwether Ad Collective</div>
  <div class="a" style="left:20px;top:42px;width:150px">
    <div class="h" style="margin-bottom:6px">Heading Goes Here</div>
    <div class="it"><span class="ic"></span><div><b>Your Text Here</b></div></div>
    <div class="it"><span class="ic g"></span><div><b>Your Text Here</b></div></div>
    <div class="it"><span class="ic"></span><div><b>Your Text Here</b></div></div>
    <div class="it"><span class="ic g"></span><div><b>Your Text Here</b></div></div>
  </div>
  <div class="ph cool" style="left:180px;top:38px;width:62px;height:152px" role="img" aria-label="Photo of a billboard in a hall"></div>
  <div class="ph crowd" style="left:246px;top:38px;width:62px;height:152px" role="img" aria-label="Photo of a corridor display"></div>
  <div class="ph warm" style="left:312px;top:38px;width:64px;height:152px" role="img" aria-label="Photo of a washroom ad frame"></div>
  <div class="foot"></div>
</section>

<section class="slide">
  <div class="s-title"><span class="u">Two</span> Column Description</div>
  <div class="brand">Bellwether Ad Collective</div>
  <div class="a" style="left:24px;top:42px;right:24px">
    <div class="lead">We are <b>Bellwether Ad Collective</b></div>
    <div class="lead">Over 1,000 Billboards | 3 Targeted Networks | Regional Coverage</div>
  </div>
  <div class="cols" style="left:24px;top:78px;right:24px;grid-template-columns:1fr 1fr;gap:20px">
    <p class="p">Our billboards sit in busy venues where guests stay for a while, so your ad is seen again and again by the same crowd. Each spot is picked for traffic and time spent.</p>
    <p class="p">Every network is gender specific, giving buyers a clear and measured audience. Rates, venue lists and proofs are ready on request for any campaign size.</p>
  </div>
  <div class="foot"></div>
</section>

<section class="slide dark">
  <div class="ph dk" style="inset:0" role="img" aria-label="Dark photo of a coffee cup on a table"></div>
  <div class="brand w">Bellwether Ad Collective</div>
  <div class="a" style="left:28px;top:108px;font-family:var(--head);font-size:10px;font-weight:600;color:#fff;letter-spacing:.5px">COFFEE BREAK</div>
  <div class="foot"></div>
</section>

<section class="slide">
  <div class="s-title"><span class="u">Three</span> Column Description</div>
  <div class="brand">Bellwether Ad Collective</div>
  <div class="a" style="left:24px;top:42px;right:24px">
    <div class="lead">We are <b>Bellwether Ad Collective</b></div>
    <div class="lead">Over 1,000 Billboards | 3 Targeted Networks | Regional Coverage</div>
  </div>
  <div class="cols" style="left:24px;top:78px;right:24px;grid-template-columns:1fr 1fr 1fr;gap:14px">
    <p class="p">Billboards sit in busy venues where guests stay a while, so your ad is seen often.</p>
    <p class="p">Each network is gender specific, giving a clear and measured audience.</p>
    <p class="p">Venue lists, rates and proofs are ready on request for any campaign.</p>
  </div>
  <div class="foot"></div>
</section>

<section class="slide">
  <div class="s-title"><span class="u">Our</span> Differences</div>
  <div class="brand">Bellwether Ad Collective</div>
  <div class="a" style="left:14px;top:42px;width:280px;height:132px;background:var(--red);border-radius:6px;padding:14px 12px">
    <div class="it" style="width:170px"><span class="ic" style="background:#fff"></span><div><b style="color:#fff">Captive audience in every venue.</b></div></div>
    <div class="it" style="width:170px"><span class="ic" style="background:#fff"></span><div><b style="color:#fff">Gender specific placement.</b></div></div>
    <div class="it" style="width:170px"><span class="ic" style="background:#fff"></span><div><b style="color:#fff">High traffic spots across Canada.</b></div></div>
    <div class="it" style="width:170px"><span class="ic" style="background:#fff"></span><div><b style="color:#fff">Simple rates and quick proofs.</b></div></div>
  </div>
  <div class="ph amber" style="left:200px;top:70px;width:112px;height:76px;border:3px solid #fff" role="img" aria-label="Photo of a framed indoor billboard"></div>
  <div class="foot"></div>
</section>

<section class="slide">
  <div class="ph crowd" style="inset:0" role="img" aria-label="Photo of a man looking at an indoor ad in a busy venue"></div>
  <div class="a" style="left:240px;top:28px;width:136px;height:150px;background:#fff;padding:14px 12px">
    <div class="brand st" style="margin-bottom:12px">Bellwether Ad Collective</div>
    <div class="big-t" style="font-size:12px">Your Title<br>Goes Here</div>
    <p class="p" style="margin-top:8px">Short line of sample text goes in this space.</p>
  </div>
  <div class="foot"></div>
</section>

<section class="slide">
  <div class="s-title">Your Title <span class="u">Goes Here</span></div>
  <div class="brand">Bellwether Ad Collective</div>
  <div class="a" style="left:18px;top:46px;width:150px">
    <div class="it"><span class="ic"></span><div><b>Service Number One</b><p>Short line of text.</p></div></div>
    <div class="it"><span class="ic g"></span><div><b>Service Number Two</b><p>Short line of text.</p></div></div>
    <div class="it"><span class="ic"></span><div><b>Service Number Three</b><p>Short line of text.</p></div></div>
  </div>
  <div class="a" style="left:180px;top:42px;right:16px">
    <div style="display:flex;gap:6px;margin-bottom:8px"><span class="num" style="width:24px;height:30px;font-size:14px">1</span><div style="flex:1;background:var(--panel);padding:5px"><p class="p" style="color:#eee">Short line of sample text here.</p></div></div>
    <div style="display:flex;gap:6px;margin-bottom:8px"><span class="num" style="width:24px;height:30px;font-size:14px">2</span><div style="flex:1;background:var(--red);padding:5px"><p class="p" style="color:#fde">Short line of sample text here.</p></div></div>
    <div style="display:flex;gap:6px"><span class="num" style="width:24px;height:30px;font-size:14px">3</span><div style="flex:1;background:var(--panel);padding:5px"><p class="p" style="color:#eee">Short line of sample text here.</p></div></div>
  </div>
  <div class="foot"></div>
</section>

<section class="slide">
  <div class="s-title"><span class="u">Four</span> Bullets with Paragraph</div>
  <div class="brand">Bellwether Ad Collective</div>
  <div class="cols" style="left:18px;top:48px;width:206px;grid-template-columns:1fr 1fr;gap:10px">
    <div class="it"><span class="ic g"></span><div><b>Your Text Here</b><p>Short sample text.</p></div></div>
    <div class="it"><span class="ic g"></span><div><b>Your Text Here</b><p>Short sample text.</p></div></div>
    <div class="it"><span class="ic"></span><div><b>Your Text Here</b><p>Short sample text.</p></div></div>
    <div class="it"><span class="ic g"></span><div><b>Your Text Here</b><p>Short sample text.</p></div></div>
  </div>
  <div class="a" style="left:236px;top:48px;right:18px"><div class="h" style="margin-bottom:6px">Heading Goes Here</div><p class="p">Our billboards sit in busy venues where guests stay for a while, so your ad is seen often by the same crowd in each spot.</p></div>
  <div class="foot"></div>
</section>

<section class="slide">
  <div class="s-title"><span class="u">Your</span> Title</div>
  <div class="brand">Bellwether Ad Collective</div>
  <div class="a" style="left:14px;top:46px;width:104px"><div class="h" style="margin-bottom:6px">Heading Goes Here</div><p class="p">Short text about this venue and the crowd that passes through it daily.</p></div>
  <div class="ph cool" style="left:124px;top:38px;width:120px;height:152px" role="img" aria-label="Photo of a lit hallway display"></div>
  <div class="a" style="left:254px;top:46px;right:10px">
    <div class="it"><span class="ic"></span><div><b>Your Text Here</b></div></div>
    <div class="it"><span class="ic g"></span><div><b>Your Text Here</b></div></div>
    <div class="it"><span class="ic"></span><div><b>Your Text Here</b></div></div>
    <div class="it"><span class="ic g"></span><div><b>Your Text Here</b></div></div>
  </div>
  <div class="foot"></div>
</section>

<section class="slide">
  <div class="s-title"><span class="u">Text</span> &amp; Bullet Area</div>
  <div class="brand">Bellwether Ad Collective</div>
  <div class="a" style="left:18px;top:46px;width:150px"><div class="h" style="margin-bottom:6px">Heading Goes Here</div><p class="p">Our billboards sit in busy venues where guests stay a while, so your ad is seen often by the same crowd.</p></div>
  <div class="cols" style="left:186px;top:46px;right:14px;grid-template-columns:1fr 1fr;gap:6px">
    <div class="it"><span class="ic"></span><div><b>Your Text Here</b><p>Short text.</p></div></div>
    <div class="it"><span class="ic g"></span><div><b>Your Text Here</b><p>Short text.</p></div></div>
    <div class="it"><span class="ic g"></span><div><b>Your Text Here</b><p>Short text.</p></div></div>
    <div class="it"><span class="ic"></span><div><b>Your Text Here</b><p>Short text.</p></div></div>
    <div class="it"><span class="ic"></span><div><b>Your Text Here</b><p>Short text.</p></div></div>
    <div class="it"><span class="ic g"></span><div><b>Your Text Here</b><p>Short text.</p></div></div>
  </div>
  <div class="foot"></div>
</section>

<section class="slide">
  <div class="brand" style="left:12px;right:auto">Bellwether Ad Collective</div>
  <div class="a big-t" style="left:14px;top:40px;font-size:12px">Your Title<br>Goes Here</div>
  <div class="a" style="left:14px;top:76px;width:84px"><p class="p">Short text about this set of venue photos.</p></div>
  <div class="ph cool" style="left:108px;top:0;width:140px;bottom:9px" role="img" aria-label="Photo of a gym with equipment"></div>
  <div class="ph warm" style="left:252px;top:0;right:0;bottom:9px" role="img" aria-label="Photo of a fitness studio"></div>
  <div class="foot"></div>
</section>

<section class="slide">
  <div class="s-title"><span class="u">Pictures</span> with Bullets</div>
  <div class="brand">Bellwether Ad Collective</div>
  <div class="ph amber" style="left:20px;top:40px;width:106px;height:72px" role="img" aria-label="Photo of a restaurant"></div>
  <div class="ph cool" style="left:143px;top:40px;width:106px;height:72px" role="img" aria-label="Photo of a hall display"></div>
  <div class="ph crowd" style="left:266px;top:40px;width:106px;height:72px" role="img" aria-label="Photo of a bar"></div>
  <div class="cols" style="left:20px;top:122px;right:20px;grid-template-columns:1fr 1fr 1fr;gap:17px">
    <div><div class="h">Heading Goes Here</div><p class="p">Short line of sample text.</p></div>
    <div><div class="h">Heading Goes Here</div><p class="p">Short line of sample text.</p></div>
    <div><div class="h">Heading Goes Here</div><p class="p">Short line of sample text.</p></div>
  </div>
  <div class="foot"></div>
</section>

<section class="slide">
  <div class="s-title">Your Title <span class="u">Goes Here</span></div>
  <div class="brand">Bellwether Ad Collective</div>
  <div class="a" style="left:18px;top:46px;width:116px">
    <div class="it"><span class="ic"></span><div><b>Your Text Here</b></div></div>
    <div class="it"><span class="ic g"></span><div><b>Your Text Here</b></div></div>
    <div class="it"><span class="ic"></span><div><b>Your Text Here</b></div></div>
  </div>
  <div class="ph dk" style="left:140px;top:38px;width:112px;height:75px" role="img" aria-label="Photo of a pub"></div>
  <div class="ph amber" style="left:256px;top:38px;width:120px;height:75px" role="img" aria-label="Photo of a lounge"></div>
  <div class="ph crowd" style="left:140px;top:117px;width:112px;height:75px" role="img" aria-label="Photo of a dining room"></div>
  <div class="ph dk" style="left:256px;top:117px;width:120px;height:75px" role="img" aria-label="Photo of a crowded bar"></div>
  <div class="foot"></div>
</section>

<section class="slide">
  <div class="s-title"><span class="u">Paragraph</span> with Three Bullet</div>
  <div class="brand">Bellwether Ad Collective</div>
  <div class="a" style="left:20px;top:42px;right:20px">
    <div class="lead">We are <b>Bellwether Ad Collective</b></div>
    <div class="lead">Over 1,000 Billboards | 3 Targeted Networks | Regional Coverage</div>
  </div>
  <div class="cols" style="left:20px;top:80px;right:20px;grid-template-columns:1fr 1fr 1fr 1fr;gap:10px">
    <p class="p">Billboards sit in busy venues where guests stay, so ads are seen often.</p>
    <div class="it" style="flex-direction:column;align-items:center;text-align:center"><span class="ic"></span><div><b>Your Text Here</b><p>Short text here.</p></div></div>
    <div class="it" style="flex-direction:column;align-items:center;text-align:center"><span class="ic g"></span><div><b>Your Text Here</b><p>Short text here.</p></div></div>
    <div class="it" style="flex-direction:column;align-items:center;text-align:center"><span class="ic"></span><div><b>Your Text Here</b><p>Short text here.</p></div></div>
  </div>
  <div class="foot"></div>
</section>

<section class="slide dark">
  <div class="ph dk" style="inset:0" role="img" aria-label="Dark photo of a venue"></div>
  <div class="brand w">Bellwether Ad Collective</div>
  <div class="a" style="left:40px;top:88px;width:260px;height:52px;background:rgba(0,0,0,.4);text-align:center;color:#fff;padding-top:7px;border-bottom:3px solid var(--red)">
    <div style="font-size:5.5px;color:#ddd">Section Title</div>
    <div class="big-t" style="font-size:12px">Your Title Goes Here</div>
    <div style="font-size:5.5px;color:#ddd">Your Subtitle Here</div>
  </div>
  <div class="foot"></div>
</section>

<section class="slide">
  <div class="s-title"><span class="u">Multiple</span> Column Area</div>
  <div class="brand">Bellwether Ad Collective</div>
  <div class="a" style="left:40px;right:40px;top:48px;display:flex;justify-content:space-between">
    <span class="ic" style="width:22px;height:22px"></span><span class="ic g" style="width:22px;height:22px"></span><span class="ic" style="width:22px;height:22px"></span><span class="ic g" style="width:22px;height:22px"></span>
  </div>
  <div class="cols" style="left:30px;top:90px;right:30px;grid-template-columns:1fr 1fr;gap:20px">
    <div><div class="h" style="margin-bottom:4px">Heading Goes Here</div><p class="p">Short text about this column of the media kit.</p></div>
    <div><div class="h" style="margin-bottom:4px">Heading Goes Here</div><p class="p">Short text about this column of the media kit.</p></div>
  </div>
  <div class="foot"></div>
</section>

<section class="slide">
  <div class="ph dk" style="left:0;top:0;right:0;height:70px" role="img" aria-label="Photo of a lobby with screens"></div>
  <div class="brand w" style="left:12px;right:auto">Bellwether Ad Collective</div>
  <div class="a big-t" style="left:190px;top:26px;font-size:11px;color:#fff">Your Title Goes Here</div>
  <div class="ph cool" style="left:14px;top:80px;width:150px;height:100px" role="img" aria-label="Photo of a billboard display"></div>
  <div class="a" style="left:186px;top:84px;right:14px">
    <div class="it"><span class="ic"></span><div><b>Your Text Here</b><p>Short line of text.</p></div></div>
    <div class="it"><span class="ic g"></span><div><b>Your Text Here</b><p>Short line of text.</p></div></div>
    <div class="it"><span class="ic"></span><div><b>Your Text Here</b><p>Short line of text.</p></div></div>
  </div>
  <div class="foot"></div>
</section>

<section class="slide">
  <div class="brand">Bellwether Ad Collective</div>
  <div class="a big-t" style="left:14px;top:38px;font-size:12px">Video Title<br>Goes Here</div>
  <div class="a" style="left:14px;top:74px;width:96px"><p class="p">Short text about the clip shown here.</p></div>
  <svg class="a" style="left:130px;top:32px" width="240" height="160" viewBox="0 0 240 160">
    <defs><linearGradient id="scr" x1="0" y1="0" x2="1" y2="1"><stop offset="0" stop-color="#f1e3d3"/><stop offset=".55" stop-color="#b98a66"/><stop offset="1" stop-color="#4a3022"/></linearGradient></defs>
    <rect x="0" y="0" width="240" height="130" rx="4" fill="#2a2a2a"/>
    <rect x="6" y="6" width="228" height="118" fill="url(#scr)"/>
    <rect x="100" y="130" width="40" height="20" fill="#cfcfcf"/>
    <rect x="80" y="150" width="80" height="5" rx="2" fill="#bdbdbd"/>
    <rect x="104" y="48" width="32" height="24" rx="5" fill="#c8161d"/>
    <path d="M116 54 L127 60 L116 66Z" fill="#fff"/>
  </svg>
  <div class="foot"></div>
</section>

<section class="slide">
  <div class="s-title"><span class="u">Global</span> Experience</div>
  <div class="brand">Bellwether Ad Collective</div>
  <div class="ph" style="left:30px;top:38px;right:30px;height:112px;background:linear-gradient(135deg,#ececec,#bdbdbd);box-shadow:none" role="img" aria-label="World map showing office locations"></div>
  <svg class="a" style="left:30px;top:38px" width="332" height="112" viewBox="0 0 332 112"><g fill="#c8161d"><circle cx="80" cy="40" r="4"/><circle cx="110" cy="70" r="4"/><circle cx="170" cy="34" r="4"/><circle cx="200" cy="60" r="4"/><circle cx="260" cy="44" r="4"/><circle cx="280" cy="84" r="4"/></g></svg>
  <div class="a" style="left:30px;top:156px"><div class="it"><span class="ic"></span><div><b>Heading Goes Here</b><p>Short line of sample text.</p></div></div></div>
  <div class="foot"></div>
</section>

<section class="slide">
  <div class="s-title"><span class="u">Four</span> Column Area</div>
  <div class="brand">Bellwether Ad Collective</div>
  <div class="cols" style="left:16px;top:54px;right:16px;grid-template-columns:repeat(4,1fr);gap:8px">
    <div style="background:var(--grey-mid);height:110px;padding:10px 6px;text-align:center"><span class="ic" style="background:#fff"></span><p class="p" style="color:#fff;margin-top:8px">Short text in this column.</p></div>
    <div style="background:var(--red);height:130px;margin-top:-10px;padding:10px 6px;text-align:center"><span class="ic" style="background:#fff"></span><p class="p" style="color:#fff;margin-top:8px">Short text in this column.</p></div>
    <div style="background:var(--grey-light);height:110px;padding:10px 6px;text-align:center"><span class="ic g"></span><p class="p" style="margin-top:8px">Short text in this column.</p></div>
    <div style="background:var(--grey-mid);height:110px;padding:10px 6px;text-align:center"><span class="ic" style="background:#fff"></span><p class="p" style="color:#fff;margin-top:8px">Short text in this column.</p></div>
  </div>
  <div class="foot"></div>
</section>

<section class="slide">
  <div class="s-title"><span class="u">Four</span> Column Area</div>
  <div class="brand">Bellwether Ad Collective</div>
  <div class="cols" style="left:20px;top:48px;right:20px;grid-template-columns:repeat(4,1fr);gap:12px;text-align:center">
    <div><div style="width:50px;height:50px;border-radius:50%;border:5px solid var(--red);margin:0 auto 8px"></div><div class="h">Heading 1</div><p class="p">Short column text.</p></div>
    <div><div style="width:50px;height:50px;border-radius:50%;border:5px solid var(--red);margin:0 auto 8px"></div><div class="h">Heading 2</div><p class="p">Short column text.</p></div>
    <div><div style="width:50px;height:50px;border-radius:50%;border:5px solid var(--red);margin:0 auto 8px"></div><div class="h">Heading 3</div><p class="p">Short column text.</p></div>
    <div><div style="width:50px;height:50px;border-radius:50%;border:5px solid var(--red);margin:0 auto 8px"></div><div class="h">Heading 4</div><p class="p">Short column text.</p></div>
  </div>
  <div class="foot"></div>
</section>

<section class="slide">
  <div class="s-title"><span class="u">Key</span> Points Area</div>
  <div class="brand">Bellwether Ad Collective</div>
  <div class="a" style="left:20px;right:20px;top:58px;display:flex;justify-content:space-between;align-items:center">
    <span style="width:38px;height:38px;border-radius:50%;background:var(--grey-mid)"></span>
    <span style="width:38px;height:38px;border-radius:50%;background:var(--grey-mid)"></span>
    <span style="width:56px;height:56px;border-radius:50%;background:var(--red)"></span>
    <span style="width:38px;height:38px;border-radius:50%;background:var(--grey-mid)"></span>
    <span style="width:38px;height:38px;border-radius:50%;background:var(--grey-mid)"></span>
  </div>
  <div class="a" style="left:60px;right:60px;top:132px;text-align:center"><div class="h">Heading Goes Here</div><p class="p">Short text that explains the key point picked above.</p></div>
  <div class="foot"></div>
</section>

<section class="slide">
  <div class="s-title"><span class="u">Process</span> Area</div>
  <div class="brand">Bellwether Ad Collective</div>
  <div class="a" style="left:20px;top:40px;width:100px"><div class="h">Process Layout</div><p class="p">Short text here.</p></div>
  <svg class="a" style="left:10px;top:60px" width="372" height="130" viewBox="0 0 372 130">
    <g font-family="Noto Serif, serif" font-size="6.5" text-anchor="middle">
      <rect x="150" y="6" width="60" height="20" rx="3" fill="#9a9a9a"/><text x="180" y="19" fill="#fff">Process 1a</text>
      <rect x="150" y="104" width="60" height="20" rx="3" fill="#9a9a9a"/><text x="180" y="117" fill="#fff">Process 1b</text>
      <rect x="10" y="55" width="56" height="20" rx="3" fill="#9a9a9a"/><text x="38" y="68" fill="#fff">Process 1</text>
      <rect x="80" y="55" width="56" height="20" rx="3" fill="#9a9a9a"/><text x="108" y="68" fill="#fff">Process 2</text>
      <rect x="150" y="55" width="60" height="20" rx="3" fill="#c8161d"/><text x="180" y="68" fill="#fff">Process 3</text>
      <rect x="224" y="55" width="56" height="20" rx="3" fill="#9a9a9a"/><text x="252" y="68" fill="#fff">Process 4</text>
      <rect x="294" y="55" width="56" height="20" rx="3" fill="#9a9a9a"/><text x="322" y="68" fill="#fff">Process 5</text>
    </g>
    <g stroke="#c8161d" stroke-width="1.5">
      <line x1="66" y1="65" x2="78" y2="65"/><line x1="136" y1="65" x2="148" y2="65"/><line x1="210" y1="65" x2="222" y2="65"/><line x1="280" y1="65" x2="292" y2="65"/>
      <line x1="180" y1="26" x2="180" y2="53"/><line x1="180" y1="77" x2="180" y2="102"/>
    </g>
  </svg>
  <div class="foot"></div>
</section>

<section class="slide">
  <div class="s-title"><span class="u">Workflow</span> Area</div>
  <div class="brand">Bellwether Ad Collective</div>
  <svg class="a" style="left:16px;top:42px" width="360" height="142" viewBox="0 0 360 142">
    <path d="M10 80 C40 10 80 10 100 80" fill="none" stroke="#c8161d" stroke-width="14"/>
    <path d="M100 80 C120 150 170 150 190 80" fill="none" stroke="#9a9a9a" stroke-width="14"/>
    <path d="M190 80 C220 10 260 10 280 80" fill="none" stroke="#c8161d" stroke-width="14"/>
    <path d="M280 80 C300 150 340 150 350 80" fill="none" stroke="#9a9a9a" stroke-width="14"/>
    <g font-family="Roboto Slab, serif" font-size="7" font-weight="700" fill="#333" text-anchor="middle">
      <text x="55" y="16">Step 1</text><text x="145" y="140">Step 2</text><text x="235" y="16">Step 3</text><text x="318" y="140">Step 4</text>
    </g>
    <g font-family="Noto Serif, serif" font-size="5" fill="#888" text-anchor="middle">
      <text x="55" y="62">Short text</text><text x="145" y="100">Short text</text><text x="235" y="62">Short text</text><text x="318" y="100">Short text</text>
    </g>
  </svg>
  <div class="foot"></div>
</section>

<section class="slide">
  <div class="s-title"><span class="u">Timeline</span></div>
  <div class="brand">Bellwether Ad Collective</div>
  <svg class="a" style="left:16px;top:40px" width="360" height="150" viewBox="0 0 360 150">
    <line x1="20" y1="75" x2="340" y2="75" stroke="#cfcfcf" stroke-width="3"/>
    <g font-family="Roboto Slab, serif" font-size="7.5" font-weight="700" fill="#fff" text-anchor="middle">
      <circle cx="40" cy="95" r="18" fill="#9a9a9a"/><text x="40" y="98">2010</text>
      <circle cx="110" cy="55" r="18" fill="#c8161d"/><text x="110" y="58">2011</text>
      <circle cx="180" cy="95" r="18" fill="#9a9a9a"/><text x="180" y="98">2012</text>
      <circle cx="250" cy="55" r="18" fill="#9a9a9a"/><text x="250" y="58">2013</text>
      <circle cx="320" cy="55" r="18" fill="#c8161d"/><text x="320" y="58">2015</text>
    </g>
    <g font-family="Noto Serif, serif" font-size="5" fill="#888" text-anchor="middle">
      <text x="40" y="128">Short text</text><text x="110" y="24">Short text</text><text x="180" y="128">Short text</text><text x="250" y="24">Short text</text><text x="320" y="24">Short text</text>
    </g>
  </svg>
  <div class="foot"></div>
</section>

<section class="slide">
  <div class="s-title"><span class="u">Bullet</span> &amp; Chart Area</div>
  <div class="brand">Bellwether Ad Collective</div>
  <svg class="a" style="left:16px;top:46px" width="170" height="130" viewBox="0 0 170 130">
    <g font-family="Noto Serif, serif" font-size="5.5" fill="#777">
      <text x="0" y="14">Option 1</text><rect x="34" y="6" width="110" height="10" fill="#c8161d"/>
      <text x="0" y="38">Option 2</text><rect x="34" y="30" width="80" height="10" fill="#9a9a9a"/>
      <text x="0" y="62">Option 3</text><rect x="34" y="54" width="126" height="10" fill="#c8161d"/>
      <text x="0" y="86">Option 4</text><rect x="34" y="78" width="60" height="10" fill="#9a9a9a"/>
      <text x="0" y="110">Option 5</text><rect x="34" y="102" width="96" height="10" fill="#c8161d"/>
    </g>
  </svg>
  <div class="a" style="left:208px;top:46px;right:14px">
    <div class="it"><span class="sq"></span><div><b>Category Here</b><p>Short text.</p></div></div>
    <div class="it"><span class="sq"></span><div><b>Category Here</b><p>Short text.</p></div></div>
    <div class="it"><span class="sq"></span><div><b>Category Here</b><p>Short text.</p></div></div>
    <div class="it"><span class="sq"></span><div><b>Category Here</b><p>Short text.</p></div></div>
  </div>
  <div class="foot"></div>
</section>

<section class="slide">
  <div class="s-title"><span class="u">Table</span> Area</div>
  <div class="brand">Bellwether Ad Collective</div>
  <div class="a" style="left:30px;top:42px;right:30px">
    <table style="font-size:5.2px;color:#555">
      <tr style="color:#fff;font-weight:700"><td style="background:#555;padding:4px">Description</td><td style="background:#888;padding:4px;text-align:center">Option 1</td><td style="background:#888;padding:4px;text-align:center">Option 2</td><td style="background:var(--red);padding:4px;text-align:center">Option 3</td></tr>
      <tr><td style="padding:3px 4px">Description 1</td><td align="center">•</td><td align="center">•</td><td align="center" style="background:#f3f3f3">•</td></tr>
      <tr style="background:#f3f3f3"><td style="padding:3px 4px">Description 2</td><td align="center">•</td><td align="center"></td><td align="center">•</td></tr>
      <tr><td style="padding:3px 4px">Description 3</td><td align="center"></td><td align="center">•</td><td align="center" style="background:#f3f3f3">•</td></tr>
      <tr style="background:#f3f3f3"><td style="padding:3px 4px">Description 4</td><td align="center">•</td><td align="center">•</td><td align="center">•</td></tr>
      <tr><td style="padding:3px 4px">Description 5</td><td align="center"></td><td align="center">•</td><td align="center" style="background:#f3f3f3">•</td></tr>
      <tr style="background:#f3f3f3"><td style="padding:3px 4px">Description 6</td><td align="center">•</td><td align="center"></td><td align="center">•</td></tr>
    </table>
  </div>
  <div class="foot"></div>
</section>

<section class="slide">
  <div class="s-title"><span class="u">Bullet</span> &amp; Chart Area</div>
  <div class="brand">Bellwether Ad Collective</div>
  <div class="a" style="left:18px;top:46px;width:170px">
    <div class="it"><span class="ic g"></span><div><b>Your Text Here</b><p>Short text.</p></div></div>
    <div class="it"><span class="ic"></span><div><b>Your Text Here</b><p>Short text.</p></div></div>
    <div class="it"><span class="ic g"></span><div><b>Your Text Here</b><p>Short text.</p></div></div>
    <div class="it"><span class="ic g"></span><div><b>Your Text Here</b><p>Short text.</p></div></div>
  </div>
  <svg class="a" style="left:210px;top:38px" width="170" height="150" viewBox="0 0 170 150">
    <circle cx="85" cy="75" r="45" fill="none" stroke="#d5d5d5" stroke-width="16"/>
    <circle cx="85" cy="75" r="45" fill="none" stroke="#c8161d" stroke-width="16" stroke-dasharray="93 190" transform="rotate(-90 85 75)"/>
    <circle cx="85" cy="75" r="45" fill="none" stroke="#8a8a8a" stroke-width="16" stroke-dasharray="70 213" stroke-dashoffset="-93" transform="rotate(-90 85 75)"/>
    <g font-family="Roboto Slab, serif" font-size="10" font-weight="700">
      <text x="118" y="16" fill="#8a8a8a">33%</text><text x="12" y="122" fill="#c8161d">25%</text><text x="140" y="92" fill="#8a8a8a">60%</text>
    </g>
  </svg>
  <div class="foot"></div>
</section>

<section class="slide">
  <div class="ph dk" style="left:0;top:0;width:110px;bottom:0" role="img" aria-label="Dark photo of an office"></div>
  <div class="a big-t" style="left:0;bottom:20px;width:110px;padding:8px;background:rgba(0,0,0,.55);color:#fff;font-size:8px;border-left:3px solid var(--red)">Meet Our Team</div>
  <div class="brand">Bellwether Ad Collective</div>
  <div class="a" style="left:200px;top:24px;display:flex;gap:8px;align-items:center">
    <div role="img" aria-label="Portrait of a team member" style="width:40px;height:40px;border-radius:50%;background:var(--ph-warm)"></div>
    <div style="font-size:5.5px;line-height:1.6"><b>Avery Lin</b><br><span style="color:var(--red)">Director</span></div>
  </div>
  <div class="a" style="left:130px;top:90px;right:14px;display:grid;grid-template-columns:1fr 1fr;gap:14px">
    <div style="display:flex;gap:6px;align-items:center"><div role="img" aria-label="Portrait of a team member" style="width:34px;height:34px;border-radius:50%;background:var(--ph-crowd)"></div><div style="font-size:5.2px;line-height:1.5"><b>Morgan Hale</b><br>Sales</div></div>
    <div style="display:flex;gap:6px;align-items:center"><div role="img" aria-label="Portrait of a team member" style="width:34px;height:34px;border-radius:50%;background:var(--ph-warm)"></div><div style="font-size:5.2px;line-height:1.5"><b>Riley Park</b><br>Design</div></div>
    <div style="display:flex;gap:6px;align-items:center"><div role="img" aria-label="Portrait of a team member" style="width:34px;height:34px;border-radius:50%;background:var(--ph-warm)"></div><div style="font-size:5.2px;line-height:1.5"><b>Jordan Vale</b><br>Media</div></div>
    <div style="display:flex;gap:6px;align-items:center"><div role="img" aria-label="Portrait of a team member" style="width:34px;height:34px;border-radius:50%;background:var(--ph-crowd)"></div><div style="font-size:5.2px;line-height:1.5"><b>Casey Moor</b><br>Accounts</div></div>
  </div>
  <div class="foot"></div>
</section>

<section class="slide">
  <div class="s-title"><span class="u">Pricing</span> Structure</div>
  <div class="brand">Bellwether Ad Collective</div>
  <div class="a" style="left:22px;top:40px;right:22px">
    <table style="font-size:5.5px;color:#555">
      <tr style="font-weight:700"><td style="padding:4px;font-family:var(--head);font-size:6.5px;color:#333">Choose Your Plan</td><td style="background:var(--red);color:#fff;text-align:center;padding:4px">BASIC</td><td style="background:#9a9a9a;color:#fff;text-align:center">GOLD</td><td style="background:#9a9a9a;color:#fff;text-align:center">PREMIUM</td></tr>
      <tr><td style="padding:3px 4px">▸ Description One</td><td align="center" style="background:#fbe5e5">✓</td><td align="center" style="background:#eee">✓</td><td align="center" style="background:#eee">✓</td></tr>
      <tr><td style="padding:3px 4px">▸ Description Two</td><td align="center" style="background:#fbe5e5">✓</td><td align="center" style="background:#eee">✓</td><td align="center" style="background:#eee">✓</td></tr>
      <tr><td style="padding:3px 4px">▸ Description Three</td><td align="center" style="background:#fbe5e5"></td><td align="center" style="background:#eee">✓</td><td align="center" style="background:#eee">✓</td></tr>
      <tr><td style="padding:3px 4px">▸ Description Four</td><td align="center" style="background:#fbe5e5"></td><td align="center" style="background:#eee"></td><td align="center" style="background:#eee">✓</td></tr>
      <tr><td style="padding:3px 4px">▸ Description Five</td><td align="center" style="background:#fbe5e5"></td><td align="center" style="background:#eee"></td><td align="center" style="background:#eee">✓</td></tr>
      <tr style="font-weight:700"><td style="padding:5px 4px;color:#333">Price</td><td align="center" style="background:var(--red);color:#fff">$299</td><td align="center" style="background:#9a9a9a;color:#fff">$499</td><td align="center" style="background:#9a9a9a;color:#fff">$799</td></tr>
    </table>
  </div>
  <div class="foot"></div>
</section>

<section class="slide dark">
  <div class="ph cool" style="inset:0;filter:brightness(.55)" role="img" aria-label="Photo of a ceiling and hall"></div>
  <div class="a" style="left:14px;top:10px;width:150px;height:22px;background:#fff;display:flex;align-items:center;justify-content:center"><span class="brand st">Bellwether Ad Collective</span></div>
  <div class="band-red" style="left:14px;top:40px;width:128px;bottom:9px;padding:12px 10px;font-size:5.2px;line-height:1.9">
    <div class="big-t" style="font-size:10px;margin-bottom:8px">Our Contact</div>
    ⌂ 120 Harbour Lane, Suite 4<br>Halifax, NS B3H 0A1<br>✆ (902) 555-0148<br>✉ hello@foxglovepromotions.ca<br>⊕ foxglovepromotions.ca
  </div>
  <div class="a" style="left:196px;top:108px;width:180px;text-align:right;color:#fff">
    <div class="big-t" style="font-size:19px;font-weight:700">THANK YOU</div>
    <div style="font-size:5.5px;color:#ddd">For Your Time Today</div>
  </div>
  <div class="foot"></div>
</section>

</main>
</body>
</html>
```